Business Card Re-Design

Consulting Company: To build a high performance organization, you need great leaders at all levels throughout your organization. The Northvale Talent Growth Studio engages, inspires, and educates current and future leaders to step beyond the ordinary and deliver exceptional results. This new breed of leaders will motivate your staff to leave the safety of complacency behind and come together to build an extraordinary organization. The current trend has been to ask our people to do more with fewer resources. People have been stepping up to the challenge, but more is required to ensure success with a new work paradigm. We work with your management team to build a successful strategy that will make your organization more effective. NTGS then supports your management team by providing a comprehensive set of proven services to empower your entire organization to successfully execute new strategies.Let NTGS help you optimize your organization’s individual and team performance today!

Target Market(s)

Federal, State and Local Government / Non profit

Industry/Entity Type

Management Consulting

Contact Information for Business Card

NTGS, inc (Northvale Talent Growth Studio) Optimizing Individual and Organizational Performance

Colors
fee18a
ec1f27
474747
fbf289

Requirements
Must have
• Professional and high quality feel

```html
<!DOCTYPE html>
<html lang="en">
<head>
<meta charset="utf-8">
<title>Northvale Talent Growth Studio — Business Card</title>
<link rel="stylesheet" href="https://fonts.googleapis.com/css2?family=Ubuntu:wght@400;700&display=swap">
<style>
  :root {
    --backdrop: #4a3426;
    --card: #fbfbf9;
    --ink: #474747;
    --ink-soft: #5c5c5c;
    --accent: #fee18a;
    --divider: #d9d9d6;
  }
  * { box-sizing: border-box; margin: 0; padding: 0; }
  html, body {
    width: 1200px;
    height: 913px;
    overflow: hidden;
  }
  body {
    background: var(--backdrop);
    font-family: "Ubuntu", sans-serif;
    position: relative;
  }
  .business-card {
    position: absolute;
    left: 250px;
    top: 256px;
    width: 700px;
    height: 400px;
    background: var(--card);
    box-shadow: 0 14px 40px rgba(0, 0, 0, 0.45);
    color: var(--ink);
  }
  .brand {
    position: absolute;
    left: 60px;
    top: 128px;
    width: 250px;
    display: flex;
    align-items: center;
    gap: 16px;
  }
  .brand-square {
    flex: none;
    width: 56px;
    height: 56px;
    background: var(--accent);
  }
  .brand-name {
    font-weight: 700;
    font-size: 21px;
    line-height: 1.2;
    color: var(--ink);
  }
  .divider {
    position: absolute;
    left: 338px;
    top: 70px;
    width: 1px;
    height: 260px;
    background: linear-gradient(to bottom, transparent, var(--divider) 20%, var(--divider) 80%, transparent);
  }
  .contact {
    position: absolute;
    left: 380px;
    top: 92px;
  }
  .person-name {
    font-weight: 700;
    font-size: 20px;
    letter-spacing: 0.02em;
    text-transform: uppercase;
    color: var(--ink);
  }
  .person-role {
    font-size: 14px;
    color: var(--ink-soft);
    margin-top: 4px;
    margin-left: 14px;
  }
  .address {
    font-style: normal;
    font-size: 14px;
    line-height: 1.4;
    color: var(--ink-soft);
    margin-top: 16px;
    margin-left: 36px;
  }
  .contact-lines {
    list-style: none;
    margin-top: 18px;
    margin-left: 56px;
  }
  .contact-lines li {
    display: flex;
    align-items: center;
    gap: 8px;
    font-size: 14px;
    line-height: 1.6;
    color: var(--ink-soft);
  }
  .contact-icon {
    width: 14px;
    height: 14px;
    flex: none;
  }
</style>
</head>
<body>
  <main class="business-card">
    <div class="brand">
      <span class="brand-square" aria-hidden="true"></span>
      <span class="brand-name">Northvale Talent Growth Studio</span>
    </div>

    <div class="divider" aria-hidden="true"></div>

    <section class="contact">
      <h1 class="person-name">Marcus L. Avery</h1>
      <p class="person-role">President / CEO</p>
      <address class="address">
        4270 Linden Crest Way<br>
        Fairhollow, MD 20918
      </address>
      <ul class="contact-lines">
        <li>
          <svg class="contact-icon" viewBox="0 0 14 14" aria-hidden="true">
            <circle cx="7" cy="7" r="7" fill="#474747"/>
            <path d="M4.3 3.6c.4-.3.8-.2 1 .2l.6 1.1c.2.4.1.7-.2.9l-.4.3c.3.8.9 1.5 1.7 1.9l.3-.4c.2-.3.6-.4.9-.2l1.1.6c.4.2.5.6.2 1l-.5.6c-.4.4-1 .5-1.6.2C5.6 9 4.3 7.6 3.6 5.8c-.2-.6 0-1.2.4-1.6z" fill="#fbfbf9"/>
          </svg>
          <span>301.555.0148</span>
        </li>
        <li>
          <svg class="contact-icon" viewBox="0 0 14 14" aria-hidden="true">
            <circle cx="7" cy="7" r="7" fill="#474747"/>
            <rect x="5" y="3.3" width="4" height="7.4" rx="0.8" fill="#fee18a"/>
            <rect x="5.7" y="4.2" width="2.6" height="4.6" fill="#474747"/>
          </svg>
          <span>301.555.0193</span>
        </li>
        <li>
          <svg class="contact-icon" viewBox="0 0 14 14" aria-hidden="true">
            <circle cx="7" cy="7" r="7" fill="#474747"/>
            <rect x="3.5" y="4.5" width="7" height="5" rx="0.6" fill="#fee18a"/>
            <path d="M3.7 4.8L7 7.4l3.3-2.6" fill="none" stroke="#474747" stroke-width="0.8"/>
          </svg>
          <span>grow@northvalestudio.com</span>
        </li>
      </ul>
    </section>
  </main>
</body>
</html>
```